Power Point make-over

We need an immediate turn around on this power point project. The presentation needs a make-over. The project includes:
1. Creating uniformity in font, colors, etc.
2. Enhancing charts and graphs.
3. Producing a better layout.
4. Some sildes can be combines.
5. The "notes" on certain slides should appear on the slide.
6. Add Tern Ridge Consulting logo- maybe as footer.

Finally- Each section (Chart your Path- Talent Compass- QRN exercise) of the power point is used in the same presentation so it needs uniformity but it does not require a segway. These exercises are also used individually for shorter presentations, so I need them to be able to stand alone. Ultimately, I need to be able to edit the power point as needed.

Target Market(s)

CEO, Executives

Industry/Entity Type

Consulting

Requirements
Must have
• The project includes:

Nice to have
• I prefer a plain white background.

```html
<!DOCTYPE html>
<html lang="en">
<head>
<meta charset="utf-8">
<title>Tern Ridge Consulting – Slide Make-over</title>
<link rel="stylesheet" href="https://fonts.googleapis.com/css2?family=Aladin&family=Questrial&family=Lora:ital@1&display=swap">
<style>
  :root {
    --stage: #e6e6e6;
    --stage-light: #f7f7f7;
    --sky: #2a8fdc;
    --sky-mid: #63b3ee;
    --sky-pale: #d7ecfb;
    --slide-base: #f3f9fe;
    --navy: #1c3f7a;
    --ink: #2b3c55;
    --axis: #d23a3a;
    --brand: #3b6e58;
    --brand-grey: #7a8a86;
    --white: #ffffff;
  }
  * { box-sizing: border-box; margin: 0; padding: 0; }
  html, body { width: 1200px; height: 1000px; overflow: hidden; }
  body {
    position: relative;
    background: radial-gradient(ellipse at 50% 45%, var(--stage-light) 0%, var(--stage) 75%);
    font-family: "Questrial", sans-serif;
    color: var(--ink);
  }
  .slide {
    position: absolute;
    width: 520px; height: 390px;
    background: linear-gradient(180deg, var(--slide-base) 0%, var(--sky-pale) 70%, #a9d4f4 100%);
    box-shadow: 0 6px 18px rgba(0,0,0,.25);
    overflow: hidden;
  }
  .slide--formula { left: 50px; top: 40px; }
  .slide--path { left: 630px; top: 230px; background: linear-gradient(180deg, var(--sky) 0%, var(--sky-mid) 45%, #a9d4f4 100%); }
  .slide--thinking { left: 50px; top: 490px; }
  .slide__band { position: absolute; left: 0; top: 0; width: 100%; height: 120px; }
  .slide__title {
    position: absolute; left: 0; right: 0; top: 14px;
    text-align: center;
    font-family: "Aladin", cursive;
    font-size: 38px; letter-spacing: 1px;
    color: var(--white);
    line-height: 1;
  }
  .slide--thinking .slide__title { font-size: 32px; top: 12px; line-height: 1.05; }
  .slide--path .slide__title { top: 22px; }
  .slide__footer {
    position: absolute; right: 10px; bottom: 10px;
    display: flex; align-items: center; gap: 4px;
    background: var(--white);
    padding: 3px 6px;
    font-family: "Questrial", sans-serif;
    font-size: 9px; color: var(--brand);
  }
  .slide__footer::before { content: ""; width: 10px; height: 10px; border-radius: 50%; background: var(--brand); }

  /* Formula */
  .def { position: absolute; font-size: 12px; line-height: 1.45; width: 220px; }
  .def b { font-family: "Lora", serif; color: var(--navy); }
  .def--talent { left: 40px; top: 130px; }
  .def--investment { left: 60px; top: 185px; }
  .def--strength { left: 80px; top: 255px; }
  .equation { position: absolute; left: 296px; top: 200px; display: flex; align-items: center; gap: 6px; }
  .equation__term {
    width: 54px; height: 40px; border-radius: 50%;
    background: var(--navy); color: var(--white);
    display: flex; align-items: center; justify-content: center;
    font-size: 8px;
  }
  .equation__op { color: #8ba2c2; font-size: 20px; font-weight: bold; }

  /* Chart */
  .chart { position: absolute; left: 0; top: 0; }
  .chart__label { font-family: "Lora", serif; font-style: italic; font-size: 11px; fill: var(--ink); }

  /* Thinking */
  .notes { position: absolute; left: 34px; top: 120px; right: 30px; list-style: none; font-size: 10.5px; line-height: 1.35; }
  .notes li { position: relative; padding-left: 14px; margin-bottom: 9px; }
  .notes li::before { content: "❖"; position: absolute; left: 0; top: 0; color: var(--sky); font-size: 9px; }
  .notes li.quote { padding-left: 0; }
  .notes li.quote::before { content: none; }
  .notes b { color: var(--navy); }
  .quote { text-align: center; font-family: "Lora", serif; font-style: italic; font-size: 11px; margin: -2px 0 10px; }

  .brand-mark {
    position: absolute; right: 40px; bottom: 40px;
    display: flex; align-items: center; gap: 14px;
    font-family: "Questrial", sans-serif;
    font-size: 40px; color: var(--brand-grey);
  }
  .brand-mark::before { content: ""; width: 56px; height: 56px; border-radius: 50%; background: var(--brand-grey); }
</style>
</head>
<body>

<svg width="0" height="0" style="position:absolute">
  <defs>
    <linearGradient id="bandFill" x1="0" y1="0" x2="0" y2="1">
      <stop offset="0" stop-color="#2a8fdc"/>
      <stop offset="1" stop-color="#7cc0f1"/>
    </linearGradient>
  </defs>
</svg>

<section class="slide slide--formula">
  <svg class="slide__band" viewBox="0 0 520 120" preserveAspectRatio="none">
    <path d="M0 0H520V70C400 110 250 60 120 95C70 108 30 100 0 92Z" fill="url(#bandFill)"/>
    <path d="M0 100C120 80 260 120 520 78" stroke="#fff" stroke-opacity=".7" fill="none"/>
    <path d="M60 112C200 90 360 110 520 90" stroke="#fff" stroke-opacity=".5" fill="none"/>
  </svg>
  <h2 class="slide__title">Formula for a Strength</h2>
  <p class="def def--talent"><b>Talent</b> is your natural way of thinking, feeling or behaving.</p>
  <p class="def def--investment"><b>Investment</b> is your time spent practicing, developing your skills, and building your knowledge base.</p>
  <p class="def def--strength"><b>Strength</b> is your ability to consistently provide near perfect performance.</p>
  <div class="equation">
    <span class="equation__term">Talent</span><span class="equation__op">×</span>
    <span class="equation__term">Investment</span><span class="equation__op">=</span>
    <span class="equation__term">Strength</span>
  </div>
  <div class="slide__footer">Tern Ridge Consulting</div>
</section>

<section class="slide slide--path">
  <h2 class="slide__title">Chart your Path</h2>
  <svg class="chart" width="520" height="390" viewBox="0 0 520 390">
    <path d="M0 330C150 300 320 360 520 300" stroke="#fff" stroke-opacity=".5" fill="none"/>
    <path d="M120 370C260 330 400 350 520 330" stroke="#fff" stroke-opacity=".4" fill="none"/>
    <rect x="80" y="80" width="390" height="180" fill="#d7ecfb" fill-opacity=".45"/>
    <line x1="80" y1="78" x2="80" y2="262" stroke="var(--axis)"/>
    <line x1="80" y1="262" x2="470" y2="262" stroke="var(--axis)"/>
    <g stroke="var(--axis)">
      <line x1="100" y1="262" x2="100" y2="267"/><line x1="130" y1="262" x2="130" y2="267"/>
      <line x1="160" y1="262" x2="160" y2="267"/><line x1="190" y1="262" x2="190" y2="267"/>
      <line x1="220" y1="262" x2="220" y2="267"/><line x1="250" y1="262" x2="250" y2="267"/>
      <line x1="280" y1="262" x2="280" y2="267"/><line x1="310" y1="262" x2="310" y2="267"/>
      <line x1="340" y1="262" x2="340" y2="267"/><line x1="370" y1="262" x2="370" y2="267"/>
      <line x1="400" y1="262" x2="400" y2="267"/><line x1="430" y1="262" x2="430" y2="267"/>
      <line x1="460" y1="262" x2="460" y2="267"/>
    </g>
    <g fill="#f2c200" stroke="#a67c00">
      <circle cx="72" cy="86" r="9"/><circle cx="72" cy="172" r="9"/><circle cx="72" cy="258" r="9"/>
    </g>
    <g class="chart__label" text-anchor="end">
      <text transform="translate(104 276) rotate(-35)">Marriage</text>
      <text transform="translate(134 276) rotate(-35)">Parenting</text>
      <text transform="translate(164 276) rotate(-35)">Work/Career</text>
      <text transform="translate(194 276) rotate(-35)">Social Life</text>
      <text transform="translate(224 276) rotate(-35)">Forum</text>
      <text transform="translate(254 276) rotate(-35)">Personal Health</text>
      <text transform="translate(284 276) rotate(-35)">Forum</text>
      <text transform="translate(314 276) rotate(-35)">Finance</text>
      <text transform="translate(344 276) rotate(-35)">Spiritual Life</text>
      <text transform="translate(374 276) rotate(-35)">Hobbies</text>
      <text transform="translate(404 276) rotate(-35)">Self</text>
      <text transform="translate(434 276) rotate(-35)">Friendships</text>
    </g>
  </svg>
  <div class="slide__footer">Tern Ridge Consulting</div>
</section>

<section class="slide slide--thinking">
  <svg class="slide__band" viewBox="0 0 520 120" preserveAspectRatio="none">
    <path d="M0 0H520V80C400 112 250 72 120 102C70 112 30 106 0 98Z" fill="url(#bandFill)"/>
    <path d="M0 106C120 86 260 124 520 86" stroke="#fff" stroke-opacity=".7" fill="none"/>
  </svg>
  <h2 class="slide__title">Change your thinking-<br>Change your world.</h2>
  <ul class="notes">
    <li><b>Purpose of the exercise:</b> To increase problem solving ability. Many of us have chronic or reoccurring problems because we stay on the same path to fixing them.</li>
    <li class="quote">"If you always do what you've always done,<br>You always get what you've always got".</li>
    <li><b>Natural tendency:</b> We tend to ruminate on problems. We think about them and re-run them in our head. We tell ourselves the same thing over and over. The way it is stored eventually hardens like cement, rendering us "stuck".</li>
    <li>This exercise can help us break free when we feel stuck. It's effective with the framing question: What situation or dilemma, if resolved, would make the most positive difference in your life?</li>
    <li>This exercise is intended to be facilitated the first time it is used.</li>
  </ul>
  <div class="slide__footer">Tern Ridge Consulting</div>
</section>

<div class="brand-mark">Tern Ridge Consulting</div>

</body>
</html>
```